We are a doctors medical practice
I need the business card to be eye catching and memorable,
to reflect professionalism, yet also warmth and care

the numbers need to be easy to see, for the elderly

and the logo also in a location that is large enough to see and be eye catching

Back of card:
opening hours:
Mon- Fri 8.30am to 6pm
Sat 9am to 4pm

rows for appontments, date and time
Updates

HiĀ 

Modification to company name

BROOKVALE KINDRED HEALTH MEDICAL PRACTICE

Thanks
Marla

Reason: I am look for a unique design that also fulfils the design brief

I have attempted to post a .eps and .ai file of the logo

Target Market(s)

needs to appeal to the majority, mainly adults

Industry/Entity Type

Medical

Contact Information for Business Card

company name: Brookvale Kindred Health Medical Practice
Name: Dr Marla Vossberg-Tait
Qualifications: MBBS, Bsci(med), FRACGP, DCH, SH&FPA, Dip Derm
Address: Shop 3/41-43 Quorrow St, Brookvale 2940
Ph: 02 9418 3052
Fax: 02 9461 8824

Requirements
Nice to have
• I like balance
gold/ silver incorporated, as well as the other colours in the logo- but not limited to these colours
a "medical" feel
Should not have
• dark or strong colours

```html
<!DOCTYPE html>
<html lang="en">
<head>
<meta charset="utf-8">
<title>Brookvale Kindred Health Medical Practice – Business Cards</title>
<link rel="stylesheet" href="https://fonts.googleapis.com/css2?family=Bebas+Neue&family=Lato:ital,wght@0,400;0,700;1,400&display=swap">
<style>
  :root {
    --stage: #47494c;
    --card: #ffffff;
    --navy: #1d4f9c;
    --blue: #2b7fc6;
    --sky: #2a9fd8;
    --green: #6cbd45;
    --pink: #e4579a;
    --rule: #e9779f;
    --bar: linear-gradient(90deg, #1f9ad6 0%, #3aa88a 35%, #7cc04a 60%, #b5a27a 80%, #e86ba6 100%);
  }
  * { box-sizing: border-box; margin: 0; padding: 0; }
  html, body { width: 1200px; height: 1000px; overflow: hidden; }
  body {
    background: var(--stage);
    font-family: "Lato", Arial, sans-serif;
    position: relative;
  }
  .card {
    position: absolute;
    background: var(--card);
    box-shadow: 0 3px 6px rgba(0,0,0,.35);
  }
  .practice-name {
    font-family: "Bebas Neue", "Oswald", sans-serif;
    font-weight: 400;
    color: var(--navy);
    text-align: center;
    letter-spacing: 1px;
    line-height: 1;
    position: absolute;
  }
  .brand-ring { position: absolute; }
  .gradient-bar { position: absolute; background: var(--bar); }

  /* Appointment card */
  .appointment-card { left: 18px; top: 297px; width: 689px; height: 425px; }
  .appointment-card .heading {
    position: absolute; left: 37px; top: 70px;
    font-size: 22px; font-weight: 700; color: var(--green);
  }
  .field {
    position: absolute; font-size: 19px; font-weight: 700; color: var(--navy);
    display: flex; align-items: flex-end;
  }
  .field .line {
    display: inline-block; border-bottom: 1.5px solid var(--rule);
    margin-left: 5px; height: 18px;
  }
  .field-name { left: 37px; top: 139px; }
  .field-date { left: 37px; top: 192px; }
  .field-time { left: 213px; top: 192px; }
  .hours-title {
    position: absolute; left: 37px; top: 258px;
    font-size: 19px; font-weight: 700; color: var(--green);
  }
  .hours {
    position: absolute; left: 37px; top: 297px;
    font-size: 16.5px; color: var(--navy);
  }
  .notice {
    position: absolute; left: 0; right: 0; top: 359px;
    text-align: center; font-size: 16.5px; font-style: italic; color: var(--pink);
  }
  .appointment-card .brand-ring { left: 445px; top: 60px; }
  .appointment-card .practice-name { left: 395px; width: 280px; top: 248px; font-size: 27px; }
  .appointment-card .gradient-bar { left: 0; right: 0; bottom: 0; height: 14px; }

  /* Doctor card */
  .doctor-card { left: 729px; top: 146px; width: 426px; height: 690px; }
  .doctor-card .brand-ring { left: 94px; top: 32px; }
  .doctor-card .practice-name { left: 0; right: 0; top: 280px; font-size: 37px; }
  .doctor-card .bar-top { left: 71px; width: 285px; top: 360px; height: 14px; }
  .doctor-card .bar-bottom { left: 72px; width: 285px; top: 629px; height: 14px; }
  .doctor-name {
    position: absolute; left: 0; right: 0; top: 393px; text-align: center;
    font-size: 24px; font-weight: 700; color: var(--navy); letter-spacing: .5px;
  }
  .qualifications {
    position: absolute; left: 0; right: 0; top: 424px; text-align: center;
    font-size: 19px; line-height: 27px; color: var(--green); letter-spacing: .5px;
  }
  .contact {
    position: absolute; left: 0; right: 0; top: 519px; text-align: center;
    font-size: 20px; line-height: 24px; color: var(--sky); letter-spacing: .5px;
  }
  .contact .label { color: var(--pink); font-weight: 700; }
</style>
</head>
<body>

  <section class="card appointment-card">
    <h2 class="heading">YOUR APPOINTMENT</h2>
    <div class="field field-name">Name:<span class="line" style="width:268px"></span></div>
    <div class="field field-date">Date:<span class="line" style="width:106px"></span></div>
    <div class="field field-time">Time:<span class="line" style="width:106px"></span></div>
    <h3 class="hours-title">Opening Hours:</h3>
    <p class="hours">Mon- Fri 8:30 am to 6 pm, Sat: 9 am to 4 pm</p>
    <p class="notice">If you are unable to attend your appointment, please contact us as soon as possible</p>

    <svg class="brand-ring" width="170" height="170" viewBox="0 0 170 170" aria-hidden="true">
      <circle cx="85" cy="85" r="80" fill="none" stroke="var(--blue)" stroke-width="6"/>
    </svg>
    <div class="practice-name">BROOKVALE KINDRED HEALTH<br>MEDICAL PRACTICE</div>

    <div class="gradient-bar"></div>
  </section>

  <section class="card doctor-card">
    <svg class="brand-ring" width="238" height="238" viewBox="0 0 238 238" aria-hidden="true">
      <circle cx="119" cy="119" r="112" fill="none" stroke="var(--blue)" stroke-width="8"/>
    </svg>
    <div class="practice-name">BROOKVALE KINDRED HEALTH<br>MEDICAL PRACTICE</div>
    <div class="gradient-bar bar-top"></div>

    <h1 class="doctor-name">Dr. Marla Vossberg-Tait</h1>
    <p class="qualifications">MBBS, BSci(Med), FRACGP,<br>DCH, SH &amp; FPA, Dip Derm</p>

    <p class="contact">
      <span class="label">Phone:</span> 02 9418 3052<br>
      <span class="label">Fax:</span> 02 9461 8824<br>
      <span class="label">Address:</span> 3/41-43 Quorrow St,<br>
      Brookvale 2940
    </p>
    <div class="gradient-bar bar-bottom"></div>
  </section>

</body>
</html>
```